High Tech Real Estate Startup needs a business card

We are developing an innovative real estate marketing product based around advanced search and virtual reality.

We talk to people, we need business cards.

Target Market(s)

The target market is technology professionals and realtors.

Contact Information for Business Card

The information to be included will include

Name
Title
Phone Number
E-mail Address
www.quelzo.com

It should use simple iconography for each one of those fields.

Font styles to use
Other font styles liked:
• Co, Jubilat, Avenir

Colors

Designer to choose colors to be used in the design.

Requirements
Must have
• Clean aesthetic,
• Good use of negative space.
• It should use our company logo, shown in the attached file. It is able to use the negative of that logo (coloured font and white background) and I have attached other acceptable accent colours in a swatch file.
Should not have
• Should not be too busy
• No extraneous text (slogans, tag lines etc)

```html
<!DOCTYPE html>
<html lang="en">
<head>
<meta charset="utf-8">
<title>Quelzo Business Card</title>
<link rel="stylesheet" href="https://fonts.googleapis.com/css2?family=Montserrat:wght@500&family=Arimo:wght@700&display=swap">
<style>
  :root {
    --crimson: #bc1142;
    --coral: #f27b56;
    --blue: #0a8dbf;
    --lime: #d6ce63;
    --amber: #f6b454;
    --white: #ffffff;
    --backdrop: #e6e6e8;
  }
  html, body {
    margin: 0;
    padding: 0;
    overflow: hidden;
  }
  .canvas {
    position: relative;
    width: 1200px;
    height: 530px;
    background: var(--backdrop);
    overflow: hidden;
  }
  .card {
    position: absolute;
    top: 105px;
    width: 560px;
    height: 320px;
    overflow: hidden;
  }
  .card--front {
    left: 30px;
    background: var(--crimson);
    display: flex;
    align-items: center;
    justify-content: center;
  }
  .card--back {
    left: 610px;
    background: var(--coral);
  }
  .wordmark {
    font-family: "Montserrat", sans-serif;
    font-weight: 500;
    letter-spacing: 0.04em;
    margin: 0;
    line-height: 1;
  }
  .card--front .wordmark {
    color: var(--white);
    font-size: 96px;
  }
  .accent-field {
    position: absolute;
    inset: 0;
    width: 560px;
    height: 320px;
  }
  .contact {
    position: absolute;
    left: 24px;
    top: 20px;
    margin: 0;
    padding: 0;
    list-style: none;
    font-family: "Arimo", sans-serif;
    font-weight: 700;
    font-size: 21px;
    line-height: 30px;
    color: var(--white);
  }
  .card--back .wordmark {
    position: absolute;
    right: 16px;
    bottom: 12px;
    color: var(--crimson);
    font-size: 38px;
  }
</style>
</head>
<body>
  <main class="canvas">
    <section class="card card--front" aria-label="Card front">
      <p class="wordmark">QUELZO</p>
    </section>

    <section class="card card--back" aria-label="Card back">
      <svg class="accent-field" viewBox="0 0 560 320" role="img" aria-label="Decorative colour accent area">
        <defs>
          <linearGradient id="accent-fade" x1="0.35" y1="0.2" x2="1" y2="1">
            <stop offset="0" stop-color="#0a8dbf"/>
            <stop offset="0.35" stop-color="#f6b454"/>
            <stop offset="0.7" stop-color="#fbe3c8"/>
            <stop offset="1" stop-color="#ffffff"/>
          </linearGradient>
        </defs>
        <polygon fill="url(#accent-fade)" points="60,320 560,20 560,320"/>
      </svg>
      <ul class="contact">
        <li class="contact__name">Name</li>
        <li class="contact__title">Title</li>
        <li class="contact__phone">Phone Number</li>
        <li class="contact__email">E-mail Address</li>
        <li class="contact__web">www.quelzo.com</li>
      </ul>
      <p class="wordmark">QUELZO</p>
    </section>
  </main>
</body>
</html>
```